Patient Engagement Solution

We need an attractive and easy-to-use GUI for patients and clinicians, which includes screens and icons. The application has been named Quorvix. I have our corporate logo attached as well.
I have attached the screens that the developer has used to create the solution, but we all know they miss the target when it comes to the creative stuff.
If it helps, I can supply some competitor's screens as a guide - please let me know.

Target Market(s)

Patients and Clinicians

Industry/Entity Type

Healthcare/Hospitals

Font styles to use
Other font styles liked:
• Easy to Read

Requirements
Must have
• Attractive, easy to use graphical user interface. Screen size is usually 22" 16:9
Nice to have
• Inviting and interesting look
Should not have
• Complicated hard to navigate screens

```html
<!DOCTYPE html>
<html lang="en">
<head>
<meta charset="utf-8">
<title>Quorvix – Applications</title>
<link rel="stylesheet" href="https://fonts.googleapis.com/css2?family=Quicksand:wght@500;600&display=swap">
<style>
  :root{
    --bg-dark:#2f2f2f;
    --bg-mid:#4a4a4a;
    --bg-light:#5e5e5e;
    --tile:rgba(255,255,255,0.07);
    --tile-active:#232323;
    --accent:#e8262c;
    --accent-light:#f25a5e;
    --text:#ffffff;
    --rule:#5a5a5a;
  }
  *{margin:0;padding:0;box-sizing:border-box}
  html,body{width:1200px;height:675px;overflow:hidden;background:var(--bg-dark)}
  body{font-family:"Quicksand",sans-serif;color:var(--text);position:relative}
  .backdrop{
    position:absolute;inset:0;
    background:
      radial-gradient(ellipse 500px 300px at 620px 420px, rgba(120,120,120,.45), transparent 70%),
      radial-gradient(ellipse 420px 200px at 250px 520px, rgba(110,110,110,.35), transparent 70%),
      linear-gradient(160deg,#3a3a3a 0%,var(--bg-mid) 45%,#333 80%,#2c2c2c 100%);
  }
  .header{position:absolute;left:120px;top:45px;height:67px;display:flex;align-items:center}
  .home-btn{
    width:89px;height:67px;border-radius:34px;
    background:linear-gradient(135deg,var(--accent-light),var(--accent));
    display:flex;align-items:center;justify-content:center;
  }
  .crumb-sep{margin-left:34px}
  .page-title{margin-left:38px;font-size:36px;font-weight:500;letter-spacing:.5px}
  .divider{position:absolute;left:120px;top:142px;width:960px;height:2px;background:var(--rule)}
  .app-grid{
    position:absolute;left:120px;top:174px;
    display:grid;grid-template-columns:repeat(5,180px);grid-auto-rows:135px;gap:15px;
  }
  .app-tile{
    background:var(--tile);position:relative;
    display:flex;flex-direction:column;align-items:center;
  }
  .app-tile svg{position:absolute;top:29px;width:38px;height:38px;fill:none;stroke:var(--text);stroke-width:1.6;stroke-linecap:round;stroke-linejoin:round}
  .app-tile .label{position:absolute;top:82px;font-size:21px;font-weight:500;letter-spacing:.4px}
  .app-tile.is-active{background:var(--tile-active);outline:2px solid var(--accent);outline-offset:-1px}
</style>
</head>
<body>
  <div class="backdrop" role="img" aria-label="Dimmed photo of a stethoscope resting on an open medical notebook"></div>

  <header class="header">
    <div class="home-btn">
      <svg width="30" height="30" viewBox="0 0 24 24" fill="none" stroke="#fff" stroke-width="2.2" stroke-linejoin="round"><path d="M4 10.5 12 4l8 6.5V20H4z"/><path d="M10 20v-5h4v5"/></svg>
    </div>
    <svg class="crumb-sep" width="16" height="24" viewBox="0 0 16 24" fill="none" stroke="#fff" stroke-width="2" stroke-linecap="round"><path d="M4 4l8 8-8 8"/></svg>
    <h1 class="page-title">Applications</h1>
  </header>
  <div class="divider"></div>

  <main class="app-grid">
    <div class="app-tile is-active">
      <svg viewBox="0 0 24 24"><rect x="2" y="6.5" width="14" height="11" rx="2.5"/><path d="M16 11l5-3v8l-5-3"/></svg>
      <span class="label">Video Calls</span>
    </div>
    <div class="app-tile">
      <svg viewBox="0 0 24 24"><circle cx="12" cy="4" r="1.8"/><path d="M12 7v6M7 11l5-2 5 2M6 20l6-5 6 5M4 20h16"/></svg>
      <span class="label">Relax</span>
    </div>
    <div class="app-tile">
      <svg viewBox="0 0 24 24"><circle cx="12" cy="12" r="9"/><path d="M12 3c-3 3-3 15 0 18M12 3c3 3 3 15 0 18M4 9h16M4 15h16"/></svg>
      <span class="label">Internet</span>
    </div>
    <div class="app-tile">
      <svg viewBox="0 0 24 24"><path d="M6 3v5a4 4 0 0 0 8 0V3"/><path d="M10 12v3a4 4 0 0 0 8 0v-2"/><circle cx="18" cy="11" r="2"/></svg>
      <span class="label">Clinical</span>
    </div>
    <div class="app-tile">
      <svg viewBox="0 0 24 24"><path d="M2 9l10-4 10 4-10 4z"/><path d="M6 11v4c2 2 10 2 12 0v-4M20 10v6"/></svg>
      <span class="label">Education</span>
    </div>
    <div class="app-tile">
      <svg viewBox="0 0 24 24"><circle cx="7" cy="5" r="2.5"/><rect x="5.5" y="10" width="3" height="11" rx="1.5"/><path d="M14 3v6a3 3 0 0 0 6 0V3M17 3v6"/><rect x="15.5" y="12" width="3" height="9" rx="1.5"/></svg>
      <span class="label">Meal</span>
    </div>
    <div class="app-tile">
      <svg viewBox="0 0 24 24"><rect x="5" y="3" width="14" height="18" rx="1.5"/><path d="M5 17h14M9 3v0"/></svg>
      <span class="label">Books</span>
    </div>
    <div class="app-tile">
      <svg viewBox="0 0 24 24"><circle cx="12" cy="12" r="3"/><path d="M12 2.5l2 2.6 3.2-.6.6 3.2 2.7 1.9-1.5 2.4 1.5 2.4-2.7 1.9-.6 3.2-3.2-.6-2 2.6-2-2.6-3.2.6-.6-3.2-2.7-1.9L5 12 3.5 9.6l2.7-1.9.6-3.2 3.2.6z"/></svg>
      <span class="label">Settings</span>
    </div>
    <div class="app-tile">
      <svg viewBox="0 0 24 24"><path d="M8 3h8v4H8zM8 7c0 5 8 5 8 0"/><path d="M4 21v-4a4 4 0 0 1 4-4h8a4 4 0 0 1 4 4v4zM12 13v8"/></svg>
      <span class="label">Concierge</span>
    </div>
    <div class="app-tile">
      <svg viewBox="0 0 24 24"><path d="M6 3l3 1 1 4-2 1.5a11 11 0 0 0 6.5 6.5L16 14l4 1 1 3-2 3C10 21 3 14 3 5z"/><path d="M14 3a7 7 0 0 1 7 7M14 6.5a3.5 3.5 0 0 1 3.5 3.5"/></svg>
      <span class="label">Phone</span>
    </div>
    <div class="app-tile">
      <svg viewBox="0 0 24 24"><path d="M3 8V4h4M17 4h4v4M21 16v4h-4M7 20H3v-4M6 12h12"/></svg>
      <span class="label">Barcode</span>
    </div>
    <div class="app-tile">
      <svg viewBox="0 0 24 24"><circle cx="12" cy="4.5" r="2.5"/><path d="M12 7v7"/><rect x="3" y="14" width="18" height="6" rx="3"/><path d="M15 17h.01M18 17h.01"/></svg>
      <span class="label">Games</span>
    </div>
    <div class="app-tile">
      <svg viewBox="0 0 24 24"><circle cx="12" cy="5" r="2.5"/><path d="M12 21l-6-6a3.3 3.3 0 0 1 6-3 3.3 3.3 0 0 1 6 3z"/></svg>
      <span class="label">My Care</span>
    </div>
    <div class="app-tile">
      <svg viewBox="0 0 24 24"><rect x="4" y="3" width="16" height="18" rx="1"/><path d="M9 3v18M15 3v18M4 8h16M4 12h16M4 16h16"/></svg>
      <span class="label">Movies</span>
    </div>
  </main>
</body>
</html>
```